Church needs a very simple, quality infographic to communicate their process

I just updated the brief with two images of a design idea that I like which I would like to see worked into my brief.
Considering those new pics, I would remove the words "up, in, out" and put in "god, the church, the world". I would put "connect in every direction" somewhere in the design. I would try to represent how we want to connect each person in each of those directions. Lastly, I would try to show a connection between those three things and a person.
Design Needs:A simple infographic that clearly communicates our discipleship pathway without requiring additional explanation. Discipleship Process:• In order for someone in our church to be completely discipled they must “connect in every direction”. They must connect …o Up to God o In to the Churcho Out to the WorldTone and Manner:• The main objective is that someone new to the church could look at the infographic and understand that our church wants to help them connect up to God, in to the church, and out to the world and that’s what they are supposed to do. • Intuitive and obvious to understand.• Simple and clear.• Same color as our logo and values (if possible). • Our church’s mission is “Connecting Young Families to Christ” so our focus is to reach out to families while not being exclusive to others. • Our church’s core values are: Equipping, Serving, Belonging, Missional Living, Spirit-living• Our target audience is families with school-aged kids. • Our website is www.lakerowchapel.ca • Our church is an evangelical Christian church about 50 years old, located in Mississauga, Canada, and recently went through a church relaunch where we came up with a new mission, vision, and values, and now our discipleship pathway. • I would like the infographic to have a real quality to it which reflects the amount of effort and care we put into crafting our discipleship pathway and how important it is going forward. Further Requests:• I intend to place this infographic on a wall in the main auditorium (5 feet x 5 feet) and be able to place it on documents, posters, website, etc.• Needs to be quality enough to scale way up and resize. • Will need the graphic completed by May 14th.Please contact Lead Pastor, Darren Holloway darren@lakerowchapel.ca

```html
<!DOCTYPE html>
<html lang="en">
<head>
<meta charset="utf-8">
<title>Connect in Every Direction – Lakerow Family Chapel</title>
<link rel="stylesheet" href="https://fonts.googleapis.com/css2?family=Montserrat:wght@600;700;800&display=swap">
<style>
  :root {
    --ink-title: #58595b;
    --ink-label: #3a3a3a;
    --ink-name: #231f20;
    --orange: #f59426;
    --blue: #1177bd;
    --purple: #90298d;
    --link-grey: #c9cacc;
    --field-grey: #eeeff0;
    --white: #ffffff;
  }
  html, body {
    margin: 0;
    padding: 0;
    overflow: hidden;
    background: var(--white);
  }
  .canvas {
    width: 1200px;
    height: 1200px;
    position: relative;
    overflow: hidden;
    background: var(--white);
  }
  .canvas svg {
    display: block;
    width: 1200px;
    height: 1200px;
  }
  .headline {
    font-family: "Montserrat", sans-serif;
    font-weight: 800;
    font-size: 134px;
    fill: var(--ink-title);
  }
  .direction-label {
    font-family: "Montserrat", sans-serif;
    font-weight: 700;
    font-size: 54px;
    letter-spacing: 1px;
    fill: var(--ink-label);
  }
  .church-name {
    font-family: "Montserrat", sans-serif;
    font-weight: 600;
    font-size: 60px;
    fill: var(--ink-name);
  }
  .link-field { fill: var(--field-grey); }
  .link-line {
    fill: none;
    stroke: var(--link-grey);
    stroke-width: 14;
    stroke-linejoin: round;
  }
  .icon-line {
    fill: none;
    stroke: var(--white);
    stroke-width: 16;
    stroke-linecap: round;
    stroke-linejoin: round;
  }
</style>
</head>
<body>
<main class="canvas">
  <svg viewBox="0 0 1920 1920" xmlns="http://www.w3.org/2000/svg">

    <text class="headline" x="966" y="233" text-anchor="middle">CONNECT in</text>
    <text class="headline" x="966" y="375" text-anchor="middle">Every Direction</text>

    <g class="pathway">
      <polygon class="link-field" points="966,622 746,1032 1189,1032"/>
      <polygon class="link-line" points="966,622 746,1032 1189,1032"/>

      <g class="node node--god">
        <circle cx="966" cy="622" r="140" fill="var(--blue)"/>
        <line class="icon-line" x1="966" y1="695" x2="966" y2="550"/>
        <polyline class="icon-line" points="916,600 966,550 1016,600"/>
      </g>

      <g class="node node--world">
        <circle cx="746" cy="1032" r="140" fill="var(--orange)"/>
        <circle cx="746" cy="1032" r="18" fill="var(--white)"/>
        <line class="icon-line" x1="746" y1="990" x2="746" y2="935"/>
        <polyline class="icon-line" points="724,957 746,935 768,957"/>
        <line class="icon-line" x1="746" y1="1074" x2="746" y2="1129"/>
        <polyline class="icon-line" points="724,1107 746,1129 768,1107"/>
        <line class="icon-line" x1="704" y1="1032" x2="649" y2="1032"/>
        <polyline class="icon-line" points="671,1010 649,1032 671,1054"/>
        <line class="icon-line" x1="788" y1="1032" x2="843" y2="1032"/>
        <polyline class="icon-line" points="821,1010 843,1032 821,1054"/>
      </g>

      <g class="node node--church">
        <circle cx="1189" cy="1032" r="140" fill="var(--purple)"/>
        <polyline class="icon-line" points="1200,962 1250,962 1250,1102 1200,1102"/>
        <line class="icon-line" x1="1110" y1="1032" x2="1205" y2="1032"/>
        <polyline class="icon-line" points="1175,1002 1205,1032 1175,1062"/>
      </g>
    </g>

    <text class="direction-label" x="1135" y="574">Up to God</text>
    <text class="direction-label" x="280" y="1013">Out to</text>
    <text class="direction-label" x="280" y="1079">the World</text>
    <text class="direction-label" x="1397" y="1013">In to</text>
    <text class="direction-label" x="1397" y="1079">the Church</text>

    <circle class="church-mark" cx="966" cy="1610" r="110" fill="var(--purple)"/>
    <text class="church-name" x="966" y="1810" text-anchor="middle">Lakerow Family Chapel</text>
  </svg>
</main>
</body>
</html>
```